Business card for a plastic surgeon

i need a business card for a plastic surgeon. I have two adresses. The card should communicate safety, simmetry, beauty and with soft colors.
What i want in the card:
- my logo: Letters "R"and "B" (picture uploaded)
- my name: Renato Bastiani
- my registration: CRM 507 219
- my adresses and phone numbers (2):
- Av Dr Teixeira Lopes, 2710, sala 305 - Vila Olímpia | São Paulo/ SP - Phone: 11 4172-5036
- Al. Itapeva, 47, 3 andar - Alphaville | Barueri/ SP - Phone: 11 6350-2481

- my social network: site, facebook and instagram

Target Market(s)

people (95% girls and women) that want cosmetic procedures and plastic surgery

Industry/Entity Type

Business

Contact Information for Business Card

The card should communicate safety, simmetry, beauty and with soft colors.
Beige, brown, gray, rosy are some options. Color is free

Font styles to use
Serif

Requirements
Must have
• - my logo: Letters "R"and "B" (picture uploaded)
• - my name: Renato Bastiani
• - my registration: CRM 507 219
• - my adresses and phone numbers (2):
• - Av Dr Teixeira Lopes, 2710, sala 305 - Vila Olímpia | São Paulo/ SP - Phone: 11 4172-5036
• - Al. Itapeva, 47, 3 andar - Alphaville | Barueri/ SP - Phone: 11 6350-2481
• - my social network: site, facebook and instagram
Should not have
• other images (only my logo)

```html
<!DOCTYPE html>
<html lang="pt-BR">
<head>
<meta charset="utf-8">
<title>Renato Bastiani – Business Card</title>
<link rel="stylesheet" href="https://fonts.googleapis.com/css2?family=EB+Garamond:ital,wght@0,400;1,400&display=swap">
<style>
  :root {
    --stage: #ececec;
    --card-front: #ffffff;
    --card-back: #a08872;
    --ink-light: #ffffff;
    --ink-brown: #a08872;
  }
  * { margin: 0; padding: 0; box-sizing: border-box; }
  html, body { width: 1200px; height: 586px; overflow: hidden; background: var(--stage); }
  body { position: relative; font-family: "EB Garamond", Garamond, serif; }

  .card { position: absolute; top: 129px; width: 502px; height: 301px; }
  .card--front { left: 61px; background: var(--card-front); }
  .card--back { left: 619px; background: var(--card-back); color: var(--ink-light); }

  .front-mark {
    position: absolute; inset: 0;
    display: flex; align-items: center; justify-content: center; gap: 12px;
    color: var(--ink-brown); font-size: 30px; font-weight: 400;
  }
  .front-mark__dot { width: 12px; height: 12px; border-radius: 50%; background: var(--ink-brown); }

  .holder-name {
    position: absolute; top: 38px; left: 0; width: 100%;
    text-align: center; font-size: 27px; font-weight: 400;
  }
  .holder-role {
    position: absolute; top: 74px; left: 121px; width: 260px;
    display: flex; align-items: center; gap: 6px;
    font-style: italic; font-size: 11px; letter-spacing: 3.6px;
  }
  .holder-role::before, .holder-role::after { content: ""; flex: 1; height: 1px; background: var(--ink-light); }
  .registration { position: absolute; top: 103px; width: 100%; text-align: center; font-size: 11px; }

  .social {
    position: absolute; top: 167px; left: 0; width: 100%;
    display: flex; justify-content: center; align-items: center; gap: 6px; font-size: 12px;
  }
  .social__dot { width: 10px; height: 10px; border-radius: 50%; background: var(--ink-light); }

  .contact { position: absolute; font-size: 12px; line-height: 17px; }
  .contact--alphaville { left: 39px; top: 216px; }
  .contact--vila-olimpia { left: 232px; top: 216px; }
  .contact__row { display: flex; align-items: flex-start; gap: 6px; margin-bottom: 6px; }
  .contact__icon { width: 17px; height: 17px; flex: none; }
</style>
</head>
<body>
  <section class="card card--front">
    <div class="front-mark"><span class="front-mark__dot"></span><span>Renato Bastiani</span></div>
  </section>

  <section class="card card--back">
    <h1 class="holder-name">Renato Bastiani</h1>
    <p class="holder-role">Owner &amp; Founder</p>
    <p class="registration">CRM 507 219</p>

    <p class="social"><span class="social__dot"></span><span>@renatobastiani</span></p>

    <div class="contact contact--alphaville">
      <div class="contact__row">
        <svg class="contact__icon" viewBox="0 0 20 20"><circle cx="10" cy="10" r="10" fill="#fff"/><path d="M5 9c0-2 2-3 5-3s5 1 5 3h-2.5V8h-5v1z M6.5 10h7l1 4h-9z" fill="#a08872"/></svg>
        <span>11 6350-2481</span>
      </div>
      <div class="contact__row">
        <svg class="contact__icon" viewBox="0 0 20 20"><circle cx="10" cy="10" r="10" fill="#fff"/><path d="M10 4a4 4 0 0 0-4 4c0 3 4 8 4 8s4-5 4-8a4 4 0 0 0-4-4z" fill="#a08872"/><circle cx="10" cy="8" r="1.5" fill="#fff"/></svg>
        <span>Al. Itapeva, 47, 3 andar<br>Alphaville | Barueri/ SP</span>
      </div>
    </div>

    <div class="contact contact--vila-olimpia">
      <div class="contact__row">
        <svg class="contact__icon" viewBox="0 0 20 20"><circle cx="10" cy="10" r="10" fill="#fff"/><path d="M5 9c0-2 2-3 5-3s5 1 5 3h-2.5V8h-5v1z M6.5 10h7l1 4h-9z" fill="#a08872"/></svg>
        <span>11 4172-5036</span>
      </div>
      <div class="contact__row">
        <svg class="contact__icon" viewBox="0 0 20 20"><circle cx="10" cy="10" r="10" fill="#fff"/><path d="M10 4a4 4 0 0 0-4 4c0 3 4 8 4 8s4-5 4-8a4 4 0 0 0-4-4z" fill="#a08872"/><circle cx="10" cy="8" r="1.5" fill="#fff"/></svg>
        <span>Av Dr Teixeira Lopes, 2710, sala 305<br>Vila Olímpia | São Paulo/ SP</span>
      </div>
    </div>
  </section>
</body>
</html>
```